Orva Business Card

we need a business card for flooring business called Orva Flooring, the design should be black and white. we have 2 locations

Ellbrook Showroom
527 Kellerman Road,
Ellbrook VIC 3168

Carrowdale Showroom
462 Bramwell Hwy,
Carrowdale VIC 3287

email : sales@orvaflooring.com.au
(03) 9471 2830

Please inform we sell , Laminate, Hybrid, Timber, carpet and commercial flooring

```html
<!DOCTYPE html>
<html lang="en">
<head>
<meta charset="utf-8">
<title>Orva Flooring — Business Card</title>
<link rel="stylesheet" href="https://fonts.googleapis.com/css2?family=Poppins:wght@300;400;500;600&display=swap">
<style>
  :root {
    --backdrop: #2b2b2e;
    --card-white: #ffffff;
    --card-black: #221f20;
    --ink: #1c1a1b;
    --paper: #ffffff;
    --muted: #d9d9d9;
  }
  * { margin: 0; padding: 0; box-sizing: border-box; }
  html, body {
    width: 1200px; height: 801px; overflow: hidden;
    background: var(--backdrop);
    font-family: "Poppins", sans-serif;
  }
  .canvas { position: relative; width: 1200px; height: 801px; }
  .card {
    position: absolute; top: 235px;
    width: 540px; height: 330px;
    box-shadow: 0 14px 30px rgba(0,0,0,.45);
  }

  .card-front {
    left: 45px; background: var(--card-white); color: var(--ink);
    display: flex; flex-direction: column; align-items: center;
  }
  .front-brand { margin-top: 92px; text-align: center; line-height: 1; }
  .brand-name {
    font-weight: 400; font-size: 44px; letter-spacing: 5px; text-transform: uppercase;
  }
  .brand-sub {
    display: block; margin-top: 10px;
    font-weight: 400; font-size: 24px; letter-spacing: 4px; text-transform: uppercase;
  }
  .front-tagline {
    position: absolute; bottom: 34px; left: 0; right: 0; text-align: center;
    font-size: 13px; font-weight: 400; letter-spacing: .3px;
  }

  .card-back { left: 615px; background: var(--card-black); color: var(--paper); }
  .contact { position: absolute; left: 34px; top: 42px; width: 250px; }
  .person-name {
    font-weight: 600; font-size: 21px; letter-spacing: 1px; text-transform: uppercase; line-height: 1.1;
  }
  .person-role { font-weight: 300; font-size: 14px; margin-bottom: 18px; }
  .contact-row { display: flex; align-items: flex-start; gap: 8px; margin-bottom: 16px; }
  .contact-row .icon {
    width: 14px; display: flex; flex-direction: column; gap: 6px; padding-top: 4px;
  }
  .contact-row .icon svg { width: 12px; height: 12px; fill: var(--paper); }
  .contact-row .divider { width: 1px; align-self: stretch; background: var(--muted); opacity: .7; }
  .contact-row p { font-size: 13px; font-weight: 400; line-height: 1.45; }
  .badge {
    position: absolute; right: 28px; top: 28px;
    width: 262px; height: 262px; border-radius: 50%;
    background: var(--paper); color: var(--ink);
    display: flex; flex-direction: column; align-items: center; justify-content: center;
    text-align: center; line-height: 1;
  }
  .badge .brand-name { font-size: 38px; }
  .badge .brand-sub { font-size: 21px; }
</style>
</head>
<body>
<main class="canvas">

  <section class="card card-front" aria-label="Business card front">
    <div class="front-brand">
      <span class="brand-name">Orva</span>
      <span class="brand-sub">Flooring</span>
    </div>
    <p class="front-tagline">we sell , Laminate, Hybrid, Timber, carpet and commercial flooring</p>
  </section>

  <section class="card card-back" aria-label="Business card back">
    <div class="contact">
      <h1 class="person-name">Jonah Merrick</h1>
      <p class="person-role">Manager</p>

      <div class="contact-row">
        <span class="icon"><svg viewBox="0 0 12 12" aria-hidden="true"><path d="M6 0a4 4 0 0 0-4 4c0 3 4 8 4 8s4-5 4-8a4 4 0 0 0-4-4zm0 5.6A1.6 1.6 0 1 1 6 2.4a1.6 1.6 0 0 1 0 3.2z"/></svg></span>
        <span class="divider"></span>
        <p>Carrowdale Showroom<br>462 Bramwell Hwy,<br>Carrowdale VIC 3287</p>
      </div>

      <div class="contact-row">
        <span class="icon"><svg viewBox="0 0 12 12" aria-hidden="true"><path d="M6 0a4 4 0 0 0-4 4c0 3 4 8 4 8s4-5 4-8a4 4 0 0 0-4-4zm0 5.6A1.6 1.6 0 1 1 6 2.4a1.6 1.6 0 0 1 0 3.2z"/></svg></span>
        <span class="divider"></span>
        <p>Ellbrook Showroom<br>527 Kellerman Road,<br>Ellbrook VIC 3168</p>
      </div>

      <div class="contact-row">
        <span class="icon">
          <svg viewBox="0 0 12 12" aria-hidden="true"><path d="M0 2h12v8H0z"/><path d="M0.6 2.4l5.4 4 5.4-4" stroke="var(--card-black)" stroke-width="1" fill="none"/></svg>
          <svg viewBox="0 0 12 12" aria-hidden="true"><path d="M2.5 0.5l2 2.6-1.2 1.3c.7 1.6 2 2.9 3.6 3.6l1.3-1.2 2.6 2-1.2 2.2C5 10.8 1.2 7 .3 1.7z"/></svg>
        </span>
        <span class="divider"></span>
        <p>sales@orvaflooring.com.au<br>(03) 9471 2830</p>
      </div>
    </div>

    <div class="badge">
      <span class="brand-name">Orva</span>
      <span class="brand-sub">Flooring</span>
    </div>
  </section>

</main>
</body>
</html>
```